Insurance company needs a business card design

We need a business card design for a Massachusetts-based insurance company Veloria Insurance, LLC. We provide auto insurance to Hispanic (Spanish- or Portuguese-speaking) immigrants in the United States. We will give these business cards to auto dealers where such customers typically go to purchase vehicles. We will provide a solution to the dealers to provide easy insurance to the customers buying cars at their dealerships. Veloria is the Spanish word for protection.
Contact Information for Business Card
Name, Designation, Company Name, Address, Phone Number, Email, Website
Look and feel
Each slider illustrates characteristics of the customer's brand and the style your logo design should communicate.

```html
<!DOCTYPE html>
<html lang="en">
<head>
<meta charset="utf-8">
<title>Veloria Insurance – Business Card</title>
<link rel="stylesheet" href="https://fonts.googleapis.com/css2?family=Roboto:wght@500;700&display=swap">
<style>
  :root {
    --backdrop: #c9c9c9;
    --navy: #02497c;
    --navy-text: #0d3a6e;
    --orange: #f0800e;
    --blob: #e6eff5;
    --paper: #ffffff;
    --faint-mark: #e9ecf3;
  }
  * { margin: 0; padding: 0; box-sizing: border-box; }
  html, body { width: 1200px; height: 1000px; overflow: hidden; }
  body {
    background: var(--backdrop);
    font-family: "Roboto", Arial, sans-serif;
    position: relative;
  }
  .card {
    position: absolute;
    width: 590px;
    height: 337px;
    overflow: hidden;
  }
  .card-front { left: 102px; top: 120px; background: var(--paper); }
  .card-back  { left: 500px; top: 535px; background: var(--navy); }

  .front-blob { position: absolute; left: 0; top: 0; }
  .front-mark {
    position: absolute;
    right: -70px; top: 70px;
    width: 300px; height: 300px;
    border-radius: 50%;
    background: var(--faint-mark);
  }
  .brand-small {
    position: absolute;
    left: 24px; top: 36px;
    display: flex; align-items: center; gap: 8px;
  }
  .brand-square { width: 16px; height: 16px; background: var(--orange); }
  .brand-small .brand-name {
    font-size: 22px; font-weight: 700; color: var(--navy-text); letter-spacing: 1px;
  }
  .identity {
    position: absolute; left: 32px; top: 122px;
    color: var(--navy-text); font-weight: 700; font-size: 19px; line-height: 26px;
  }
  .contacts {
    position: absolute; left: 32px; top: 226px;
    list-style: none;
    color: var(--orange); font-weight: 700; font-size: 13px; line-height: 17px;
  }
  .contacts li { display: flex; align-items: flex-start; gap: 10px; margin-bottom: 8px; }
  .contacts svg { flex: none; width: 17px; height: 17px; margin-top: 0; }

  .brand-large {
    position: absolute; left: 0; right: 0; top: 0; bottom: 0;
    display: flex; align-items: center; justify-content: center; gap: 16px;
  }
  .brand-large .brand-square { width: 34px; height: 34px; }
  .brand-large .brand-name {
    font-size: 60px; font-weight: 700; color: var(--paper); letter-spacing: 3px;
  }
</style>
</head>
<body>
  <section class="card card-front" aria-label="Card front">
    <svg class="front-blob" width="300" height="150" viewBox="0 0 300 150" aria-hidden="true">
      <path d="M0 0 H295 C300 40 270 70 220 70 C180 70 170 120 120 140 C70 158 20 130 0 110 Z" fill="var(--blob)"/>
    </svg>
    <div class="front-mark" aria-hidden="true"></div>

    <div class="brand-small">
      <span class="brand-square"></span>
      <span class="brand-name">VELORIA</span>
    </div>

    <div class="identity">
      <p>Name,</p>
      <p>Designation,</p>
      <p>Company Name</p>
    </div>

    <ul class="contacts">
      <li>
        <svg viewBox="0 0 24 24" fill="none" stroke="var(--navy-text)" stroke-width="2" stroke-linejoin="round"><path d="M5 3h4l2 5-2.5 1.5a11 11 0 0 0 6 6L16 13l5 2v4a2 2 0 0 1-2 2A17 17 0 0 1 3 5a2 2 0 0 1 2-2z"/></svg>
        <span>(866) 555-0193</span>
      </li>
      <li>
        <svg viewBox="0 0 24 24" fill="none" stroke="var(--navy-text)" stroke-width="2"><rect x="3" y="5" width="18" height="14" rx="1"/><path d="M3 6l9 7 9-7"/></svg>
        <span>info@veloriainsurance.com</span>
      </li>
      <li>
        <svg viewBox="0 0 24 24" fill="none" stroke="var(--navy-text)" stroke-width="2"><path d="M12 22s7-7 7-12a7 7 0 0 0-14 0c0 5 7 12 7 12z"/><circle cx="12" cy="10" r="2.5"/></svg>
        <span>48 Harbor Lane, Suite 310,<br>Quincy, MA 02169</span>
      </li>
    </ul>
  </section>

  <section class="card card-back" aria-label="Card back">
    <div class="brand-large">
      <span class="brand-square"></span>
      <span class="brand-name">VELORIA</span>
    </div>
  </section>
</body>
</html>
```